Business Card for a Mortgage Agent (myself)

I need a business card for my new job as Mortgage Agent. The Broker's logo is to be on the card as well as the brokerage License number. Not sure if to include a photo or not. Info to be on card.
Dante Roux
Mortgage Agent
Lic # M47105386
Cell: 905-614-2753
Email: danterouxk.ma@fennmail.com
Web: www.karlvostermortgages.com
TPW Brokerage Lic. # 73918

```html
<!DOCTYPE html>
<html lang="en">
<head>
<meta charset="utf-8">
<title>Dante Roux – Mortgage Agent Business Card</title>
<link href="https://fonts.googleapis.com/css2?family=Open+Sans:wght@400;600;700;800&display=swap" rel="stylesheet">
<style>
  :root {
    --backdrop: #b1d5f1;
    --card: #ffffff;
    --brand-blue: #0f55a0;
    --ink-blue: #1a4587;
    --brand-yellow: #fbcd10;
    --shadow: rgba(30, 50, 80, 0.45);
  }
  * { margin: 0; padding: 0; box-sizing: border-box; }
  html, body {
    width: 856px; height: 1200px; overflow: hidden;
    background: var(--backdrop);
    font-family: "Open Sans", Arial, sans-serif;
  }
  .card {
    position: absolute; left: 190px; width: 476px; height: 272px;
    background: var(--card); border-radius: 13px;
    box-shadow: 8px 9px 10px var(--shadow);
    overflow: hidden;
  }
  .card--front { top: 254px; }
  .card--back { top: 603px; }

  .ribbon { position: absolute; left: 24px; top: 0; width: 25px; height: 101px; }

  .agent-name {
    position: absolute; left: 62px; top: 19px;
    font-size: 24px; font-weight: 800; color: var(--ink-blue); letter-spacing: -0.3px;
  }
  .agent-title {
    position: absolute; left: 62px; top: 56px;
    font-size: 16px; font-weight: 700; color: var(--ink-blue);
  }
  .agent-licence {
    position: absolute; left: 62px; top: 84px;
    font-size: 13.5px; font-weight: 600; color: var(--ink-blue);
  }

  .brand-mark {
    position: absolute; display: flex; align-items: center; gap: 10px;
    color: var(--brand-blue); font-weight: 800;
  }
  .brand-mark__square { background: var(--brand-yellow); flex: none; }
  .card--front .brand-mark { left: 318px; top: 44px; font-size: 40px; }
  .card--front .brand-mark__square { width: 34px; height: 34px; }
  .card--back .brand-mark { left: 50%; top: 82px; transform: translateX(-50%); font-size: 72px; gap: 18px; }
  .card--back .brand-mark__square { width: 60px; height: 60px; }

  .contact-list { position: absolute; left: 24px; top: 144px; list-style: none; }
  .contact-item {
    display: flex; align-items: center; height: 25.5px;
    font-size: 13.5px; font-weight: 600; color: var(--ink-blue);
  }
  .contact-icon { width: 25px; height: 25px; margin-right: 13px; flex: none; }

  .licence-band {
    position: absolute; left: 0; top: 233px; width: 100%; height: 22px;
    display: flex; align-items: center; justify-content: center;
    font-size: 15px; font-weight: 600;
  }
  .licence-band--blue { background: var(--brand-blue); color: #fff; }
  .licence-band--yellow { background: var(--brand-yellow); color: var(--ink-blue); }
</style>
</head>
<body>

<section class="card card--front">
  <svg class="ribbon" viewBox="0 0 25 101"><polygon points="0,0 25,0 25,88 12.5,101 0,88" fill="var(--brand-yellow)"/></svg>

  <h1 class="agent-name">DANTE ROUX</h1>
  <p class="agent-title">Mortgage Agent</p>
  <p class="agent-licence">Lic # M47105386</p>

  <div class="brand-mark"><span class="brand-mark__square"></span>TPW</div>

  <ul class="contact-list">
    <li class="contact-item">
      <svg class="contact-icon" viewBox="0 0 25 25">
        <polygon points="12.5,0 25,12.5 12.5,25 0,12.5" fill="var(--brand-yellow)"/>
        <rect x="9" y="6.5" width="7" height="12" rx="1.2" fill="none" stroke="var(--ink-blue)" stroke-width="1.4"/>
        <line x1="11.5" y1="16.3" x2="13.5" y2="16.3" stroke="var(--ink-blue)" stroke-width="1.2"/>
      </svg>
      905-614-2753
    </li>
    <li class="contact-item">
      <svg class="contact-icon" viewBox="0 0 25 25">
        <polygon points="12.5,0 25,12.5 12.5,25 0,12.5" fill="var(--brand-yellow)"/>
        <g fill="none" stroke="var(--ink-blue)" stroke-width="1.2">
          <circle cx="12.5" cy="12.5" r="6"/>
          <ellipse cx="12.5" cy="12.5" rx="2.6" ry="6"/>
          <line x1="6.5" y1="12.5" x2="18.5" y2="12.5"/>
          <line x1="7.5" y1="9.5" x2="17.5" y2="9.5"/>
          <line x1="7.5" y1="15.5" x2="17.5" y2="15.5"/>
        </g>
      </svg>
      www.karlvostermortgages.com
    </li>
    <li class="contact-item">
      <svg class="contact-icon" viewBox="0 0 25 25">
        <polygon points="12.5,0 25,12.5 12.5,25 0,12.5" fill="var(--brand-yellow)"/>
        <g fill="none" stroke="var(--ink-blue)" stroke-width="1.3">
          <rect x="7" y="8.5" width="11" height="8"/>
          <polyline points="7,8.5 12.5,13 18,8.5"/>
          <line x1="7" y1="16.5" x2="11" y2="12"/>
          <line x1="18" y1="16.5" x2="14" y2="12"/>
        </g>
      </svg>
      <span>&nbsp;danterouxk.ma@fennmail.com</span>
    </li>
  </ul>

  <p class="licence-band licence-band--blue">TPW Brokerage Lic. # 73918</p>
</section>

<section class="card card--back">
  <div class="brand-mark"><span class="brand-mark__square"></span>TPW</div>
  <p class="licence-band licence-band--yellow">TPW Brokerage Lic. # 73918</p>
</section>

</body>
</html>
```